Design of a can of the adaptogenic drink brand "VellaMist" (vector)

Please take the cans from the brief and make a print-ready vector with the instructions as in the other photos.

Target Market(s)

Young, upper-middle class athlete

Industry/Entity Type

Agroalimentaire

Colors

Designer to choose colors to be used in the design.

Requirements
Must have
• Adaptogenic flawed water
Nice to have
• Sleek, classy and healthy

```html
<!DOCTYPE html>
<html lang="fr">
<head>
<meta charset="utf-8">
<title>VellaMist – Boisson Energissante</title>
<link rel="stylesheet" href="https://fonts.googleapis.com/css2?family=Archivo+Black&family=Arimo:wght@400&family=Quicksand:wght@500&display=swap">
<style>
  :root {
    --backdrop: #d4d4d4;
    --label-white: #f7f6f7;
    --brand-teal: #0f5862;
    --deep-teal: #0b4a52;
    --ink: #111111;
  }
  html, body {
    margin: 0;
    padding: 0;
    width: 1200px;
    height: 1200px;
    overflow: hidden;
    background: var(--backdrop);
  }
  .can-label {
    position: absolute;
    left: 260px;
    top: 110px;
    width: 680px;
    height: 980px;
    background: var(--label-white);
    border-radius: 24px;
    box-sizing: border-box;
    padding: 130px 80px 150px 100px;
    display: flex;
    flex-direction: column;
  }
  .brand-name {
    margin: 0;
    font-family: "Quicksand", "Trebuchet MS", sans-serif;
    font-weight: 500;
    font-size: 168px;
    line-height: 0.92;
    letter-spacing: -2px;
    color: var(--brand-teal);
  }
  .brand-name span {
    display: block;
  }
  .product-info {
    margin-top: 70px;
  }
  .product-type {
    margin: 0;
    font-family: "Archivo Black", "Arial Black", sans-serif;
    font-size: 40px;
    line-height: 1.1;
    color: var(--deep-teal);
  }
  .brand-line {
    margin: 12px 0 0;
    font-family: "Arimo", Arial, sans-serif;
    font-size: 33px;
    line-height: 1.25;
    color: var(--ink);
  }
  .volume {
    margin: auto 0 0;
    font-family: "Arimo", Arial, sans-serif;
    font-size: 36px;
    line-height: 1.2;
    color: var(--ink);
  }
</style>
</head>
<body>
  <main class="can-label">
    <h1 class="brand-name"><span>Vella</span><span>Mist</span></h1>
    <div class="product-info">
      <p class="product-type">Boisson Energissante</p>
      <p class="brand-line">Marque: VellaMist<br>Eau adaptogène</p>
    </div>
    <p class="volume">12 fl oz (355ml)</p>
  </main>
</body>
</html>
```